Veteran Owned General Contractor needs Bold New Business Cards

We are a service disabled veteran owned small business. We're a general contractor that specializes in excavation, underground utilities, site work, land clearing and demolition. We would like a fresh, simple, bold, new look for our business cards. We're open to ideas! We'd like to incorporate the following information on the card:

Company Name & Logo, Name of Person, Job Title, Office Phone, Fax, Cell Phone, Email Address, Website, SDVOSB

Our logo is included. We look forward to your thoughts.

Thank you!

Reason: Hello Due to the overwhelming response to this project, we are extending the deadline one time to allow for improved communication and feedback with the top candidates. We would like to thank everyone for their hard work and exceptional creativity! Thank you

Industry/Entity Type

Business

Contact Information for Business Card

Font styles to use
Sans Serif

Requirements
Nice to have
• As we are a veteran owned company, it would be nice to incorporate an American flag into the design. Maybe on the back?

```html
<!DOCTYPE html>
<html lang="en">
<head>
<meta charset="utf-8">
<title>Ridgeform Inc – Business Card</title>
<link rel="stylesheet" href="https://fonts.googleapis.com/css2?family=Source+Sans+3:wght@400;600&display=swap">
<style>
  :root {
    --page-bg: #e4e1de;
    --brand-green: #6cbf43;
    --card-clear: #f3f1ef;
    --text-dark: #3a3a3a;
    --text-light: #ffffff;
  }
  * { box-sizing: border-box; margin: 0; padding: 0; }
  html, body {
    width: 1200px;
    height: 900px;
    overflow: hidden;
  }
  body {
    background: var(--page-bg);
    font-family: "Source Sans 3", Arial, sans-serif;
    position: relative;
  }
  .business-card {
    position: absolute;
    left: 120px;
    top: 152px;
    width: 960px;
    height: 595px;
    display: flex;
    background: var(--card-clear);
    box-shadow: 0 10px 30px rgba(0, 0, 0, 0.12);
  }
  .contact-panel {
    width: 410px;
    height: 100%;
    background: var(--brand-green);
    color: var(--text-light);
    padding: 172px 0 0 48px;
  }
  .person-name {
    font-size: 34px;
    font-weight: 600;
    line-height: 1.1;
  }
  .job-title {
    font-size: 24px;
    font-weight: 400;
    margin-top: 4px;
  }
  .office-address {
    font-style: normal;
    font-size: 24px;
    line-height: 1.4;
    margin-top: 26px;
  }
  .contact-list {
    list-style: none;
    margin-top: 22px;
    font-size: 24px;
    line-height: 1.45;
  }
  .contact-list li {
    display: flex;
    align-items: center;
    gap: 14px;
  }
  .contact-icon {
    width: 20px;
    height: 20px;
    flex: none;
    fill: var(--text-light);
  }
  .brand-panel {
    flex: 1;
    display: flex;
    align-items: center;
    justify-content: center;
  }
  .brand-line {
    display: flex;
    align-items: center;
    gap: 16px;
  }
  .brand-dot {
    width: 22px;
    height: 22px;
    border-radius: 50%;
    background: var(--brand-green);
  }
  .brand-name {
    font-size: 44px;
    font-weight: 600;
    color: var(--text-dark);
    white-space: nowrap;
    line-height: 1;
  }
</style>
</head>
<body>
  <section class="business-card">
    <div class="contact-panel">
      <h1 class="person-name">Daniel Hartwell</h1>
      <p class="job-title">Managing Director</p>
      <address class="office-address">
        12345, Address Goes Here<br>
        Country Name, 123456.
      </address>
      <ul class="contact-list">
        <li>
          <svg class="contact-icon" viewBox="0 0 24 24" aria-hidden="true">
            <path d="M6.6 10.8a15.1 15.1 0 0 0 6.6 6.6l2.2-2.2a1 1 0 0 1 1-.25 11.4 11.4 0 0 0 3.6.57 1 1 0 0 1 1 1V20a1 1 0 0 1-1 1A17 17 0 0 1 3 4a1 1 0 0 1 1-1h3.5a1 1 0 0 1 1 1c0 1.25.2 2.45.57 3.57a1 1 0 0 1-.25 1z"/>
          </svg>
          <span>044-123 456 789</span>
        </li>
        <li>
          <svg class="contact-icon" viewBox="0 0 24 24" aria-hidden="true">
            <path d="M2 5h20v14H2z"/>
            <path d="M3 6l9 7 9-7" fill="none" stroke="#6cbf43" stroke-width="2"/>
          </svg>
          <span>info@webname.com</span>
        </li>
        <li>
          <svg class="contact-icon" viewBox="0 0 24 24" aria-hidden="true">
            <path d="M10.6 13.4a1 1 0 0 0 1.4 0l4-4a1 1 0 1 0-1.4-1.4l-4 4a1 1 0 0 0 0 1.4zM8.5 11.1l-2.8 2.8a3.5 3.5 0 0 0 5 5l2.8-2.8-1.4-1.4-2.8 2.8a1.5 1.5 0 0 1-2.2-2.2l2.8-2.8zm7 1.8 2.8-2.8a3.5 3.5 0 0 0-5-5l-2.8 2.8 1.4 1.4 2.8-2.8a1.5 1.5 0 0 1 2.2 2.2l-2.8 2.8z"/>
          </svg>
          <span>www.websitename.com</span>
        </li>
      </ul>
    </div>
    <div class="brand-panel">
      <div class="brand-line">
        <span class="brand-dot" aria-hidden="true"></span>
        <p class="brand-name">Ridgeform Inc</p>
      </div>
    </div>
  </section>
</body>
</html>
```